Law firm website marketed direct to many individual clients

I need someone to design a very basic website for a law firm that will be very eye catching. It's going to be a single-paged, scrolling website with a small number of folds. I have uploaded a simple word document that outlines the basics of what I thought could be the layout, but I am open to suggestion on font, size, shades of color, organization, etc. etc. Essentially the website just needs to be a very efficient and visually appealing way of conveying some simple messages.

Target Market(s)

High volumes of individuals who have gotten into a car accident and then google on their phones a lawyer to hire to represent them.

Industry/Entity Type

Legal

Number of Pages Required

1 page

Font styles to use
Serif
Sans Serif

Colors
34a7d7
85cae6
0592cd

Requirements
Must have
• Must be bright and grab the users attention with color scheme and layout. The different sections should be done in such a way that they can fit entirely onto one smart phone or tablet screen.
Nice to have
• I'd like to try and see what it looks like if in the middle somewhere there is a fold that says "MEET YOUR ATTORNEYS" and includes individual photos of two attorneys, one on the left side and one on the right. And then a small bio section on them. I don't want the photos to include a square or rectangle background, I want the person in the photo to be superimposed on top of whatever pattern or background you have in the fold.
Should not have
• Do not want too much text. Anything more than 2 sentences in any single place is unacceptable.

```html
<!DOCTYPE html>
<html lang="en">
<head>
<meta charset="utf-8">
<title>Meridian Law Group</title>
<link href="https://fonts.googleapis.com/css2?family=Roboto:wght@400;500;700&family=Roboto+Condensed:wght@400&family=Raleway:wght@400;500&family=Open+Sans:wght@400;600&display=swap" rel="stylesheet">
<style>
:root{
  --blue:#1388c9;
  --blue-light:#85cae6;
  --blue-mid:#34a7d7;
  --hero:#2f8fc6;
  --band:#1679b3;
  --navy:#0f3a57;
  --ink:#222;
  --footer:#1f1d1c;
  --bar:#1b8ed1;
  --white:#fff;
}
*{box-sizing:border-box;margin:0;padding:0}
html,body{width:710px;height:1200px;overflow:hidden;background:#fff}
body{position:relative;font-family:"Roboto",Arial,sans-serif;color:var(--ink)}
.abs{position:absolute}
.center{left:0;width:710px;text-align:center}

.top-stripe{top:0;left:0;width:710px;height:3px;display:flex}
.top-stripe span{flex:1}
.top-stripe span:nth-child(1){background:var(--blue)}
.top-stripe span:nth-child(2){background:var(--blue-light)}
.top-stripe span:nth-child(3){background:var(--blue)}

.site-header{top:3px;left:0;width:710px;height:59px;background:#fff}
.brand{left:58px;top:19px;display:flex;align-items:center;gap:8px;font-family:"Roboto Condensed",sans-serif;font-size:19px;color:var(--blue)}
.brand-square{width:12px;height:12px;background:var(--blue)}
.header-phone{left:512px;top:20px;display:flex;align-items:center;gap:7px;font-family:"Roboto Condensed",sans-serif;font-size:14px;color:var(--blue)}
.menu-btn{left:626px;top:19px;width:25px;height:23px;border:1.5px solid var(--blue);border-radius:3px;display:flex;flex-direction:column;justify-content:center;align-items:center;gap:2px}
.menu-btn i{display:block;width:9px;height:1.6px;background:var(--blue)}

.hero{top:62px;left:0;width:710px;height:280px;background:linear-gradient(100deg,#3b8fc0 0%,#3597cd 45%,#2c86bd 100%)}
.hero-kicker{top:101px;font-size:16px;font-weight:500;color:#fff}
.hero-title{top:140px;font-size:32px;font-weight:700;color:#fff;letter-spacing:.3px}

.call-btn{left:250px;width:210px;height:33px;border-radius:5px;display:flex;align-items:center;font-weight:700;font-size:17px}
.call-btn .ring{width:33px;height:33px;border-radius:50%;display:flex;align-items:center;justify-content:center;margin-left:-1px;margin-right:10px}
.call-btn.light{border:1.5px solid #fff;color:#fff}
.call-btn.light .ring{background:var(--navy);border:2px solid #fff}
.call-btn.outline{border:1.5px solid var(--blue);color:var(--blue);background:#fff}
.call-btn.outline .ring{background:var(--blue)}

.learn-btn{left:313px;top:273px;width:85px;height:32px;border:1.5px solid #fff;border-radius:5px;background:var(--navy);color:#fff;font-size:12px;font-weight:500;display:flex;align-items:center;justify-content:center}

.services-title{top:369px;font-size:18px;font-weight:700;color:var(--blue)}
.services-intro{top:400px;font-size:8.5px;color:#333}
.service{display:flex;gap:0}
.service-icon{width:60px;height:60px;border:2px solid var(--blue);border-radius:50%;display:flex;align-items:center;justify-content:center;position:absolute}
.service-name{position:absolute;font-size:13.5px;font-weight:500;color:var(--blue);line-height:16px;width:220px}
.service-text{position:absolute;font-size:9px;color:#222;line-height:15px;width:190px}

.band{top:679px;left:0;width:710px;height:310px;background:linear-gradient(160deg,#1b7fbb 0%,#1a86c0 40%,#136fa8 100%)}
.band h2{font-size:20px;font-weight:700;color:#fff}
.band-text{font-family:"Raleway",sans-serif;font-size:11px;line-height:19.5px;color:#fff}

.site-footer{top:989px;left:0;width:710px;height:177px;background:linear-gradient(90deg,#1c1a19 0%,#2a2522 55%,#1c1a19 100%)}
.footer-brand{left:58px;top:1053px;display:flex;align-items:center;gap:7px;font-family:"Roboto Condensed",sans-serif;font-size:17px;color:#fff}
.footer-brand .brand-square{background:#fff;width:11px;height:11px}
.footer-h{top:1019px;font-family:"Raleway",sans-serif;font-size:11.5px;font-weight:500;color:#fff}
.quick-links{left:218px;top:1045px;list-style:none;font-family:"Raleway",sans-serif;font-size:8.5px;color:#fff;line-height:15.2px}
.quick-links li::before{content:">";margin-right:5px}
.contact-row{left:332px;display:flex;gap:8px;font-family:"Open Sans",sans-serif;font-size:8px;color:#fff;line-height:12px}
.field{border:1px solid #ddd;border-radius:2px;color:#fff;font-family:"Open Sans",sans-serif;font-size:6.5px;padding:6px 7px}
.send-btn{left:493px;top:1118px;width:70px;height:23px;background:var(--bar);color:#fff;font-family:"Open Sans",sans-serif;font-size:7px;font-weight:600;display:flex;align-items:center;justify-content:center;border-radius:1px}

.bottom-bar{top:1166px;left:0;width:710px;height:34px;background:var(--bar)}
.copyright{left:58px;top:1177px;font-family:"Open Sans",sans-serif;font-size:9px;color:#fff}
.social{top:1173px;left:563px;display:flex;gap:6px}
.social span{width:19px;height:19px;border:1.3px solid #fff;border-radius:50%}
</style>
</head>
<body>

<div class="abs top-stripe"><span></span><span></span><span></span></div>

<header class="abs site-header"></header>
<div class="abs brand"><span class="brand-square"></span>Meridian Law Group</div>
<div class="abs header-phone">
  <svg width="22" height="22" viewBox="0 0 22 22"><circle cx="11" cy="11" r="10" fill="none" stroke="#1388c9" stroke-width="1.5"/><path d="M8 6.5c.6-.4 1.2-.2 1.5.4l.8 1.5c.2.5 0 1-.4 1.3l-.5.4c.5 1.2 1.4 2.1 2.5 2.6l.4-.5c.3-.4.9-.5 1.3-.3l1.5.8c.6.3.7 1 .3 1.5-1 1.3-2.6 1.4-4.3.3-1.6-1-2.9-2.6-3.5-4.3-.4-1.4-.5-2.9.4-3.7z" fill="#1388c9"/></svg>
  504-555-0142
</div>
<div class="abs menu-btn"><i></i><i></i><i></i></div>

<section class="abs hero" role="img" aria-label="Photo of an injured elderly man on crutches with his wife, speaking with an attorney holding a clipboard, tinted blue"></section>
<p class="abs center hero-kicker">ACCIDENT? INJURED?</p>
<h1 class="abs center hero-title">“YOUR CASE. YOUR MONEY”.</h1>
<a class="abs call-btn light" style="top:204px">
  <span class="ring"><svg width="18" height="18" viewBox="0 0 20 20"><path d="M5 3c.8-.5 1.6-.3 2 .5l1.1 2c.3.6.1 1.3-.4 1.7l-.7.5c.7 1.6 1.9 2.8 3.4 3.5l.5-.7c.4-.5 1.1-.7 1.7-.4l2 1.1c.8.4.9 1.3.4 2-1.3 1.7-3.5 1.8-5.7.4-2.1-1.3-3.8-3.4-4.6-5.6C4.1 7.1 4 5 5 3z" fill="none" stroke="#fff" stroke-width="1.3"/><path d="M12 3.5a5 5 0 0 1 4.5 4.5M12 6a2.5 2.5 0 0 1 2 2" fill="none" stroke="#fff" stroke-width="1.2"/></svg></span>
  CALL 504-555-0142
</a>
<a class="abs learn-btn">Learn More</a>

<h2 class="abs center services-title">OUR SERVICES</h2>
<p class="abs center services-intro">With extensive experience in helping clients get the results that they want, our team is always just a phone call away.</p>

<div class="service-icon" style="left:64px;top:436px">
  <svg width="36" height="36" viewBox="0 0 36 36"><text x="18" y="20" text-anchor="middle" font-family="Roboto,sans-serif" font-weight="700" font-size="20" fill="#1388c9">$</text><path d="M4 28h6l5 2h8l7-5" fill="none" stroke="#1388c9" stroke-width="2.2" stroke-linecap="round"/></svg>
</div>
<h3 class="service-name" style="left:140px;top:448px">LOW FEES</h3>
<p class="service-text" style="left:140px;top:470px">We charge less, so you keep more</p>

<div class="service-icon" style="left:408px;top:436px">
  <svg width="36" height="36" viewBox="0 0 36 36"><path d="M7 19a11 11 0 0 1 22 0" fill="none" stroke="#1388c9" stroke-width="2.4"/><rect x="4" y="17" width="6" height="9" rx="2" fill="#1388c9"/><rect x="26" y="17" width="6" height="9" rx="2" fill="#1388c9"/><path d="M29 26c0 4-4 5-9 5" fill="none" stroke="#1388c9" stroke-width="1.8"/></svg>
</div>
<h3 class="service-name" style="left:484px;top:448px">FREE CONSULTATION</h3>
<p class="service-text" style="left:484px;top:470px">It's always free to talk to us.</p>

<div class="service-icon" style="left:64px;top:527px">
  <svg width="36" height="36" viewBox="0 0 36 36"><rect x="11" y="5" width="14" height="26" rx="2.5" fill="none" stroke="#1388c9" stroke-width="2.2"/><rect x="13.5" y="9" width="9" height="15" fill="#1388c9"/><circle cx="18" cy="27.5" r="1.4" fill="#1388c9"/><path d="M7 12c-1.5 2-1.5 5 0 7M29 12c1.5 2 1.5 5 0 7" fill="none" stroke="#1388c9" stroke-width="1.4"/></svg>
</div>
<h3 class="service-name" style="left:140px;top:526px">GET STARTED USING ONLY YOUR PHONE</h3>
<p class="service-text" style="left:140px;top:558px">No need to come to the office, sign up using your phone.</p>

<div class="service-icon" style="left:408px;top:527px">
  <svg width="36" height="36" viewBox="0 0 36 36"><path d="M18 7v22M11 29h14M8 11h20" stroke="#1388c9" stroke-width="2" fill="none"/><path d="M8 11l-4 9h8zM28 11l-4 9h8z" fill="none" stroke="#1388c9" stroke-width="1.6"/><path d="M4 20a4 3 0 0 0 8 0M24 20a4 3 0 0 0 8 0" fill="#1388c9"/></svg>
</div>
<h3 class="service-name" style="left:484px;top:526px">SPEAK DIRECTLY TO A LAWYER</h3>
<p class="service-text" style="left:484px;top:558px;width:180px">No staff screening. Talk right to a lawyer on your first call.</p>

<a class="abs call-btn outline" style="top:620px">
  <span class="ring"><svg width="18" height="18" viewBox="0 0 20 20"><path d="M5 3c.8-.5 1.6-.3 2 .5l1.1 2c.3.6.1 1.3-.4 1.7l-.7.5c.7 1.6 1.9 2.8 3.4 3.5l.5-.7c.4-.5 1.1-.7 1.7-.4l2 1.1c.8.4.9 1.3.4 2-1.3 1.7-3.5 1.8-5.7.4-2.1-1.3-3.8-3.4-4.6-5.6C4.1 7.1 4 5 5 3z" fill="none" stroke="#fff" stroke-width="1.3"/><path d="M12 3.5a5 5 0 0 1 4.5 4.5M12 6a2.5 2.5 0 0 1 2 2" fill="none" stroke="#fff" stroke-width="1.2"/></svg></span>
  CALL 504-555-0142
</a>

<section class="abs band" role="img" aria-label="Photo of a smiling woman relaxing outdoors, tinted blue"></section>
<h2 class="abs center" style="top:717px;font-size:20px;font-weight:700;color:#fff">NO FEE UNLESS WE WIN</h2>
<p class="abs band-text" style="left:150px;top:754px;width:410px;text-align:center">We don't get paid unless you get paid. It's as simple as that. We let our results do the talking for us</p>
<h2 class="abs center" style="top:818px;font-size:20px;font-weight:700;color:#fff">QUESTIONS ABOUT ANYTHING?</h2>
<p class="abs band-text" style="left:75px;top:856px;width:560px;text-align:center">We're here to help. Feel free to call us at 504-555-0142 to speak to one of our attorneys. With extensive experience in helping clients get the results that they want, our team is always just a phone call away.</p>
<a class="abs call-btn light" style="top:922px">
  <span class="ring"><svg width="18" height="18" viewBox="0 0 20 20"><path d="M5 3c.8-.5 1.6-.3 2 .5l1.1 2c.3.6.1 1.3-.4 1.7l-.7.5c.7 1.6 1.9 2.8 3.4 3.5l.5-.7c.4-.5 1.1-.7 1.7-.4l2 1.1c.8.4.9 1.3.4 2-1.3 1.7-3.5 1.8-5.7.4-2.1-1.3-3.8-3.4-4.6-5.6C4.1 7.1 4 5 5 3z" fill="none" stroke="#fff" stroke-width="1.3"/><path d="M12 3.5a5 5 0 0 1 4.5 4.5M12 6a2.5 2.5 0 0 1 2 2" fill="none" stroke="#fff" stroke-width="1.2"/></svg></span>
  CALL 504-555-0142
</a>

<footer class="abs site-footer" role="img" aria-label="Dark background photo of a handshake in an office"></footer>
<div class="abs footer-brand"><span class="brand-square"></span>Meridian Law Group</div>

<h4 class="abs footer-h" style="left:218px">QUICK LINK</h4>
<ul class="abs quick-links">
  <li>HOME</li><li>ABOUT</li><li>PRACTICE AREAS</li><li>BLOG</li><li>CONTACT</li>
</ul>

<h4 class="abs footer-h" style="left:331px">CONTACT US</h4>
<div class="abs contact-row" style="top:1044px">
  <svg width="9" height="11" viewBox="0 0 9 11"><path d="M4.5 0A4 4 0 0 0 .5 4c0 3 4 7 4 7s4-4 4-7a4 4 0 0 0-4-4z" fill="#fff"/><circle cx="4.5" cy="4" r="1.5" fill="#222"/></svg>
  <span>Meridian law group,<br>42 North Harbor Ave. Unit<br>Lakeside.</span>
</div>
<div class="abs contact-row" style="top:1091px">
  <svg width="9" height="10" viewBox="0 0 20 20"><path d="M5 2c.8-.5 1.6-.3 2 .5l1.1 2c.3.6.1 1.3-.4 1.7l-.7.5c.7 1.6 1.9 2.8 3.4 3.5l.5-.7c.4-.5 1.1-.7 1.7-.4l2 1.1c.8.4.9 1.3.4 2-1.3 1.7-3.5 1.8-5.7.4-2.1-1.3-3.8-3.4-4.6-5.6C3.9 6.1 4 4 5 2z" fill="#fff"/></svg>
  <span>Help : + 1800 555 0199</span>
</div>
<div class="abs contact-row" style="top:1112px;font-size:9px">
  <svg width="9" height="10" viewBox="0 0 9 10"><rect x="0" y="2" width="9" height="6" fill="#fff"/><path d="M0 2l4.5 3.5L9 2" stroke="#222" fill="none"/></svg>
  <span>info@meridianlawgroup.example</span>
</div>

<h4 class="abs footer-h" style="left:492px">CONTACT FORM</h4>
<div class="abs field" style="left:493px;top:1045px;width:77px;height:21px">Name</div>
<div class="abs field" style="left:574px;top:1045px;width:77px;height:21px">Phone</div>
<div class="abs field" style="left:493px;top:1070px;width:158px;height:39px">Enter Email Id</div>
<a class="abs send-btn">SEND MESSAGE</a>

<div class="abs bottom-bar"></div>
<p class="abs copyright">© 2016 Meridian law group. All Rights Reserved.</p>
<div class="abs social"><span></span><span></span><span></span><span></span></div>

</body>
</html>
```